High-end residential home builder needs a business card design

We need a new business card design for a small residential construction company based in Boise, Idaho. We specialize in building custom high-end homes and remodels, with a focus on great design and craftsmanship.

We would like to use our current logo, but open to new color suggestions.
Just looking for a clean, sharp, modern design that looks high-end.

Target Market(s)

Upscale clientele

Industry/Entity Type

Contractor

Contact Information for Business Card

Company: Stonehaven Custom Builders
Name: Colin Marsh
Phone number: 208 637 4120
Email: ColinMarshSCB@quillpost.net
Website: Stonehavencustombuilders.com

Font styles to use
Serif
Sans Serif

Requirements
Must have
• Company Logo
Company name
My name
My phone number
My email
Company website
Nice to have
• I have attached a few photos of cards that I really like.

```html
<!DOCTYPE html>
<html lang="en">
<head>
<meta charset="utf-8">
<title>Stonehaven Custom Builders – Business Card</title>
<link rel="stylesheet" href="https://fonts.googleapis.com/css2?family=Lato:wght@400;700;900&family=Montserrat:wght@500;600&display=swap">
<style>
  :root {
    --backdrop: #d2d3ce;
    --paper: #ffffff;
    --ink: #1c1c1c;
    --espresso: #201511;
    --espresso-light: #2c211c;
    --gold: #cc944c;
    --rule: #9a9a9a;
  }
  * { box-sizing: border-box; margin: 0; padding: 0; }
  html, body {
    width: 1200px; height: 801px; overflow: hidden;
    background: var(--backdrop);
  }
  .stage {
    width: 1200px; height: 801px;
    display: flex; align-items: center; justify-content: center; gap: 40px;
  }
  .card {
    position: relative;
    width: 540px; height: 309px;
    box-shadow: 0 10px 24px rgba(0,0,0,0.18);
    overflow: hidden;
  }

  /* Front face */
  .card--front { background: var(--paper); }
  .brand {
    position: absolute; left: 50px; top: 122px;
    display: flex; align-items: center; gap: 12px;
  }
  .brand__mark {
    width: 14px; height: 14px; background: var(--espresso); flex: none;
  }
  .brand__text { display: flex; flex-direction: column; }
  .brand__name {
    font-family: "Montserrat", sans-serif; font-weight: 600;
    font-size: 14px; letter-spacing: 3.5px; line-height: 1.2;
    text-transform: uppercase; color: var(--espresso);
    padding-bottom: 4px; border-bottom: 1px solid var(--espresso);
  }
  .brand__sub {
    font-family: "Montserrat", sans-serif; font-weight: 600;
    font-size: 8.5px; letter-spacing: 3px; line-height: 1.2;
    text-transform: uppercase; color: var(--gold);
    margin-top: 4px; padding-left: 14px;
  }
  .divider {
    position: absolute; left: 278px; top: 92px;
    width: 1px; height: 98px; background: var(--rule);
  }
  .person {
    position: absolute; left: 300px; top: 72px;
    font-family: "Lato", sans-serif;
  }
  .person__name {
    font-weight: 900; font-size: 19px; letter-spacing: 0.2px;
    text-transform: uppercase; color: var(--ink);
  }
  .person__title {
    font-weight: 400; font-size: 12px; color: var(--gold); margin-top: 1px;
  }
  .contact { list-style: none; margin-top: 12px; }
  .contact__item {
    display: flex; align-items: center; gap: 9px;
    font-size: 11.5px; color: var(--ink); line-height: 19px;
  }
  .contact__icon { width: 11px; height: 11px; flex: none; }
  .band {
    position: absolute; left: 0; right: 0; top: 246px; height: 18px;
  }
  .band__dark {
    position: absolute; left: 0; top: 0; width: 398px; height: 18px;
    background: var(--espresso);
  }
  .band__gold {
    position: absolute; left: 440px; right: 0; top: 0; height: 18px;
    background: var(--gold);
  }
  .band__seal {
    position: absolute; left: 404px; top: -8px;
    width: 30px; height: 30px; border-radius: 50%;
    background: var(--paper); border: 2px solid var(--espresso);
  }

  /* Back face */
  .card--back { background: var(--espresso); }
  .backdrop-pattern {
    position: absolute; inset: 0;
    background: radial-gradient(circle at 50% 50%, var(--espresso-light), var(--espresso) 75%);
  }
  .back-name {
    position: absolute; left: 0; right: 0; top: 50%;
    transform: translateY(-50%);
    text-align: center;
    font-family: "Montserrat", sans-serif; font-weight: 600;
    font-size: 14px; letter-spacing: 4px; line-height: 1.5;
    text-transform: uppercase; color: var(--gold);
  }
</style>
</head>
<body>
<main class="stage">
  <section class="card card--front" aria-label="Business card front">
    <div class="brand">
      <span class="brand__mark"></span>
      <div class="brand__text">
        <p class="brand__name">Stonehaven</p>
        <p class="brand__sub">Custom Builders</p>
      </div>
    </div>
    <div class="divider"></div>
    <div class="person">
      <h1 class="person__name">Colin Marsh</h1>
      <p class="person__title">President</p>
      <ul class="contact">
        <li class="contact__item">
          <svg class="contact__icon" viewBox="0 0 12 12"><path d="M3 1 L5 3.5 L4 5 Q5 7 7 8 L8.5 7 L11 9 L9.5 11 Q4 10.5 1 2.5 Z" fill="var(--gold)"/></svg>
          208 637 4120
        </li>
        <li class="contact__item">
          <svg class="contact__icon" viewBox="0 0 12 12"><rect x="0.5" y="2" width="11" height="8" fill="var(--gold)"/><path d="M0.5 2 L6 6.5 L11.5 2" fill="none" stroke="#fff" stroke-width="1"/></svg>
          ColinMarshSCB@quillpost.net
        </li>
        <li class="contact__item">
          <svg class="contact__icon" viewBox="0 0 12 12"><circle cx="6" cy="6" r="5" fill="none" stroke="var(--gold)" stroke-width="1.2"/><path d="M1 6 H11 M6 1 V11" stroke="var(--gold)" stroke-width="0.9"/></svg>
          www.Stonehavencustombuilders.com
        </li>
      </ul>
    </div>
    <div class="band">
      <div class="band__dark"></div>
      <div class="band__seal"></div>
      <div class="band__gold"></div>
    </div>
  </section>

  <section class="card card--back" aria-label="Business card back">
    <div class="backdrop-pattern" role="img" aria-label="Dark brown repeating tonal pattern covering the card back"></div>
    <p class="back-name">Stonehaven<br>Custom Builders</p>
  </section>
</main>
</body>
</html>
```